London Based Property Finding Company - have logo already

We find property for private purchasers and investors in London, UK.  We work for the BUYER, whereas estate agencies/real estate companies work for the seller. We offer a much more personalised service to UK and overseas purchasers.

We would like the following:

*A double sided business card

*A letterhead

We have attached two versions of the logo. Each logo style is set on two different coloured backgrounds. Please choose one of the two designs, whichever you prefer or feel more comfortable with, and produce one in black and one in white background.

This applies to both pieces of stationery.

THE BUSINESS CARD:

We would like the company name placed on its own on one side of the card and the contact details and what we do on the other.

e.g.

SIDE 1:

BRAMWELL PROPERTY FINDERS

SIDE 2:

Owen Bramwell

t: 0208 394 2860

m: +44(0)7932 418 507

e: info@bramwellpropertyfinders.co.uk

w: bramwellpropertyfinders.co.uk

London Property Finders and Search Agents

I will leave the layout up to you, but a minimalist layout is preferred. If you would like to put additional detial or design on the card then that is up to, but not specified.

It is optional to have the company name on side 2, but if you do use it, please make it smaller. than on the 1st side.

The design needs to be simple, professional and not too in your face.

If you are using the black background design on side 1 for the logo, then maybe a white backgounnd can be used on side 2 with a black typeface.

The type face for the contacts details should be sans serif standard typeface. Please experiment with the desciprtion.

-

THE LETTERHEAD;

You can experiment with the layout for the letterhead. e.g logo centre aligned on the top of the page with the contact details and address at the bottom of the page OR the logo, description running along a bar on the top of the page with the contact details and website address at the bottom. Please try and experiment with this, but the less 'busy', the better.

Here is info that needs to be on the letterhead.

Bramwell Property Finders

t: 0208 394 2860

m: +44(0)7932 418 507

(PLEASE NOTE; the below company info must be placed at the bottom of the page as a footer, in small text.)

Kestrand Holdings Ltd Trading as Bramwell Property Finders, a company registered in England & Wales, No.7351926 , Registered office is 41 Hollinmoor Court, Hollinmoor Road, London, SW9 3PL, t: 0208 394 2860, m: +44(0)7932 418 507, e: info@bramwellpropertyfinders.co.uk

Best of luck!

Thank you

Dear Designer,

I have now attached the supporting files to this brief.

Thanks,

Owen Bramwell
Bramwell Property Finders

```html
<!DOCTYPE html>
<html lang="en">
<head>
<meta charset="utf-8">
<title>Bramwell Property Finders – Stationery</title>
<link rel="stylesheet" href="https://fonts.googleapis.com/css2?family=Jost:wght@400;500&display=swap">
<style>
  :root {
    --ink: #000000;
    --paper: #ffffff;
    --card-edge: #6e6e6e;
    --name-maroon: #5a0d18;
    --text-font: "Jost", "Futura", sans-serif;
  }
  * { margin: 0; padding: 0; box-sizing: border-box; }
  html, body { width: 1200px; height: 917px; overflow: hidden; background: var(--paper); }
  body { position: relative; font-family: var(--text-font); color: var(--ink); }

  .section-title {
    position: absolute; top: 2px; font-size: 20px; font-weight: 400;
    letter-spacing: 2px; text-align: center; width: 300px;
  }
  .section-title--letterhead { left: 157px; }
  .section-title--card { left: 760px; letter-spacing: 1.5px; }

  /* Letterhead */
  .letterhead-bar {
    position: absolute; left: 0; top: 40px; width: 627px; height: 72px;
    background: var(--ink); color: var(--paper);
  }
  .wordmark {
    position: absolute; color: var(--paper); font-weight: 400;
    white-space: nowrap; line-height: 1;
  }
  .letterhead-bar .wordmark { left: 16px; top: 29px; font-size: 15px; letter-spacing: 2px; }
  .letterhead-contacts {
    position: absolute; left: 432px; top: 12px; list-style: none;
    font-size: 9px; line-height: 14px; letter-spacing: 0.4px;
  }
  .letterhead-footer {
    position: absolute; left: 0; width: 627px; top: 887px;
    text-align: center; font-size: 6.5px; line-height: 10px; letter-spacing: 0.3px;
  }

  /* Business cards */
  .card { position: absolute; width: 265px; height: 151px; }
  .card--front { left: 659px; background: var(--ink); }
  .card--back { left: 933px; background: var(--paper); border: 1px solid var(--card-edge); }
  .card--row1 { top: 41px; }
  .card--row2 { top: 201px; }

  .card--front .wordmark { font-size: 9.5px; letter-spacing: 1.2px; }
  .wordmark--centred { left: 0; width: 100%; text-align: center; top: 71px; }
  .wordmark--corner { right: 12px; top: 125px; }

  .card-holder {
    position: absolute; left: 12px; font-size: 12px; color: var(--name-maroon);
    letter-spacing: 0.5px; font-weight: 400;
  }
  .card-contacts {
    position: absolute; left: 12px; list-style: none;
    font-size: 8px; line-height: 12.6px; letter-spacing: 0.4px;
  }
  .card-tagline { position: absolute; left: 12px; font-size: 8px; letter-spacing: 0.6px; }
  .card--row1 .card-holder { top: 23px; }
  .card--row1 .card-contacts { top: 57px; }
  .card--row1 .card-tagline { top: 122px; }
  .card--row2 .card-holder { top: 26px; }
  .card--row2 .card-contacts { top: 58px; }
  .card--row2 .card-tagline { top: 123px; }
</style>
</head>
<body>
  <h2 class="section-title section-title--letterhead">LETTER HEAD</h2>
  <h2 class="section-title section-title--card">Business Card</h2>

  <header class="letterhead-bar">
    <span class="wordmark">BRAMWELL PROPERTY FINDERS</span>
    <ul class="letterhead-contacts">
      <li>t: 0208 394 2860</li>
      <li>m: +44(0)7932 418 507</li>
      <li>e: info@bramwellpropertyfinders.co.uk</li>
      <li>w: bramwellpropertyfinders.co.uk</li>
    </ul>
  </header>

  <footer class="letterhead-footer">
    Kestrand Holdings Ltd Trading as Bramwell Property Finders, a company registered in England &amp; Wales, No.7351926 ,<br>
    Registered office is 41 Hollinmoor Court, Hollinmoor Road, London, SW9 3PL, t: 0208 394 2860,<br>
    m: +44(0)7932 418 507, e: info@bramwellpropertyfinders.co.uk
  </footer>

  <section class="card card--front card--row1">
    <span class="wordmark wordmark--centred">BRAMWELL PROPERTY FINDERS</span>
  </section>
  <section class="card card--back card--row1">
    <p class="card-holder">Owen Bramwell</p>
    <ul class="card-contacts">
      <li>t: 0208 394 2860</li>
      <li>m: +44(0)7932 418 507</li>
      <li>e: info@bramwellpropertyfinders.co.uk</li>
      <li>w: bramwellpropertyfinders.co.uk</li>
    </ul>
    <p class="card-tagline">London Property Finders and Search Agents</p>
  </section>

  <section class="card card--front card--row2">
    <span class="wordmark wordmark--corner">BRAMWELL PROPERTY FINDERS</span>
  </section>
  <section class="card card--back card--row2">
    <p class="card-holder">Owen Bramwell</p>
    <ul class="card-contacts">
      <li>t: 0208 394 2860</li>
      <li>m: +44(0)7932 418 507</li>
      <li>e: info@bramwellpropertyfinders.co.uk</li>
      <li>w: bramwellpropertyfinders.co.uk</li>
    </ul>
    <p class="card-tagline">London Property Finders and Search Agents</p>
  </section>
</body>
</html>
```